Website redesign www.brindlecovepc.com law firm site

Need to redesign the website that I currently have to look more modern and professional. Would also like to be able to make updates and post without having a huge hassle. See current www.brindlecovepc.com. I just think that it looks very immature and it's very templated there's no ability for me to make posts or Add links or anything like that

Target Market(s)

California people looking for a powerhouse attorney in

Industry/Entity Type

Legal

Number of Pages Required

3 page

Font styles to use
Serif
Sans Serif

Colors
ec1f27
000000
ffffff

Requirements
Must have
• Must be mobile friendly. Must look professional and have ability to post links to other websites. Must have ability to post blogs or articles. Would like to be able to read my Quindral account and also have the ability to upload forms for people to download
Nice to have
• Simple design easy to use and not cluttered with too much text

```html
<!DOCTYPE html>
<html lang="en">
<head>
<meta charset="utf-8">
<title>Brindle Cove P.C — Business Law</title>
<link rel="stylesheet" href="https://fonts.googleapis.com/css2?family=Montserrat:wght@400;600;700&family=Open+Sans:wght@400;600&family=Playfair+Display:ital,wght@0,400;1,400&display=swap">
<style>
:root{
  --red:#ec1f27;
  --red-dark:#c5141b;
  --black:#000000;
  --white:#ffffff;
  --ink:#333333;
  --muted:#666666;
  --paper:#f4f2f2;
  --footer:#333333;
  --line:#222222;
}
*{box-sizing:border-box;margin:0;padding:0}
html,body{width:1200px;height:2871px;overflow:hidden}
body{position:relative;background:var(--white);font-family:"Open Sans",Arial,sans-serif;color:var(--ink)}
.abs{position:absolute}
/* top bar */
.topbar{left:0;top:0;width:1200px;height:34px;background:var(--red);color:var(--white);font-size:12px}
.topbar .contact{left:130px;top:9px;display:flex;gap:14px;align-items:center}
.topbar .social{right:130px;top:11px;display:flex;gap:12px}
.topbar .social span{width:10px;height:10px;border-radius:50%;background:var(--white);display:block}
/* header */
.header{left:0;top:34px;width:1200px;height:112px;background:var(--white);box-shadow:0 2px 6px rgba(0,0,0,.08);z-index:2}
.brand{left:150px;top:28px;font-family:"Playfair Display",serif;font-size:40px;color:var(--red);letter-spacing:1px;line-height:1}
.nav{right:130px;top:47px;display:flex;gap:34px;font-family:Montserrat,sans-serif;font-size:12px;font-weight:600;color:var(--line)}
.nav a{color:inherit;text-decoration:none;position:relative}
.nav a.active{color:var(--red)}
.nav a.active::after{content:"";position:absolute;left:-4px;right:-4px;top:57px;height:4px;background:var(--red)}
/* hero */
.hero{left:0;top:146px;width:1200px;height:440px;background:linear-gradient(90deg,#dfe3e7 0%,#c9ced3 45%,#5b5f66 70%,#2f3238 100%)}
.hero h1{left:130px;top:78px;font-family:"Playfair Display",serif;font-weight:400;font-size:34px;line-height:1.2;color:#2a2a2a}
.hero p{left:130px;top:172px;width:240px;font-size:13px;line-height:1.6;color:#222}
.btn{background:var(--red);color:var(--white);display:flex;align-items:center;justify-content:center}
.hero .btn{left:130px;top:233px;width:228px;height:59px;font-family:"Playfair Display",serif;font-size:20px;border-radius:3px}
.dots{display:flex;gap:8px}
.dots span{width:11px;height:11px;border-radius:50%;background:var(--white)}
.dots span.on{background:var(--red)}
.hero .dots{left:133px;top:316px}
/* welcome */
.welcome-art{left:130px;top:632px;width:276px;height:210px;background:radial-gradient(circle,#8a1c1c 0%,#c2a08a 55%,#ffffff 80%)}
.h2{font-family:Montserrat,sans-serif;font-weight:600;color:var(--red);text-transform:uppercase}
.welcome h2{left:459px;top:620px;font-size:31px}
.welcome .copy{left:459px;top:674px;width:554px;font-size:11px;line-height:1.9;color:#444}
.welcome .copy p+p{margin-top:14px}
.welcome .btn{left:459px;top:848px;width:107px;height:40px;font-family:Montserrat,sans-serif;font-size:12px;font-weight:700;border-radius:3px}
/* practice areas */
.practice{left:0;top:934px;width:1200px;height:466px;background:var(--paper)}
.practice h2{left:0;width:1200px;top:62px;text-align:center;font-size:29px}
.area{width:320px}
.area svg{position:absolute;left:0;top:0}
.area h3{position:absolute;left:58px;top:0;font-family:Montserrat,sans-serif;font-weight:400;font-size:19px;color:var(--black);white-space:nowrap}
.area p{position:absolute;left:58px;top:36px;width:222px;font-size:10.5px;line-height:1.85;color:#555;text-align:justify}
/* testimonial */
.quote{left:0;top:1400px;width:1200px;height:260px;background:linear-gradient(90deg,#1f2a36 0%,#3d4753 40%,#28313b 100%)}
.quote blockquote{left:120px;top:76px;width:960px;text-align:center;font-family:"Playfair Display",serif;font-style:italic;font-size:14px;line-height:2;color:var(--white)}
.quote cite{left:0;top:156px;width:1200px;text-align:center;font-family:"Playfair Display",serif;font-size:13px;color:#ddd}
.quote .dots{left:580px;top:210px}
.quote .dots span{width:7px;height:7px;background:#bbb}
.quote .dots span.on{background:var(--red)}
/* blog */
.blog h2{left:0;width:1200px;top:1705px;text-align:center;font-size:29px}
.post{width:288px}
.post .thumb{width:288px;height:147px;background:linear-gradient(135deg,#c7cdd3,#5a6270 60%,#2b2f36);border:3px solid var(--white);box-shadow:0 0 0 1px #ddd}
.post h3{margin-top:22px;font-family:Montserrat,sans-serif;font-weight:600;font-size:19px;color:var(--red);white-space:nowrap}
.post time{display:block;margin-top:12px;font-size:10px;color:#555}
.post p{margin-top:14px;font-size:11px;line-height:1.8;color:#666}
.post a{display:block;margin-top:12px;font-size:11px;color:var(--red);text-decoration:none}
/* partners */
.partners{left:0;top:2160px;width:1200px;height:190px;background:var(--paper)}
.badge{top:41px;height:107px;background:var(--white);border:1px solid #ccc;display:flex;align-items:center;justify-content:center}
.badge span{display:block;background:#c8ccd4}
/* contact */
.map{left:0;top:2350px;width:1200px;height:464px;background:linear-gradient(135deg,#e8e4dc 0%,#dde3d6 40%,#e9e6de 70%,#d9e3ea 100%)}
.card{left:130px;top:2408px;width:938px;height:337px;background:var(--white)}
.card h2{position:absolute;left:25px;top:24px;font-size:28px}
.card .intro{position:absolute;left:25px;top:80px;width:400px;font-size:10.5px;line-height:1.8;color:#333}
.card .label{position:absolute;font-size:12px;color:var(--red)}
.card .value{position:absolute;font-size:11px;color:#333;display:flex;gap:8px;align-items:center}
.field{position:absolute;left:444px;width:442px;border-bottom:2px solid var(--line);font-size:10.5px;color:#222;padding-bottom:10px}
.card .btn{position:absolute;left:444px;top:228px;width:442px;height:38px;font-family:Montserrat,sans-serif;font-size:11px;font-weight:700;border-radius:3px;background:linear-gradient(#ee2a31,var(--red-dark))}
/* footer */
.footer{left:0;top:2814px;width:1200px;height:57px;background:var(--footer);color:#aaa;font-size:11px}
.footer .copy{left:130px;top:21px}
.footer .social{right:130px;top:22px;display:flex;gap:18px}
.footer .social span{width:12px;height:12px;border-radius:50%;background:#888;display:block}
</style>
</head>
<body>

<div class="abs topbar">
  <div class="abs contact">
    <svg width="11" height="11" viewBox="0 0 24 24"><path fill="#fff" d="M6.6 10.8a15 15 0 0 0 6.6 6.6l2.2-2.2a1 1 0 0 1 1-.25 11 11 0 0 0 3.6.6 1 1 0 0 1 1 1V20a1 1 0 0 1-1 1A17 17 0 0 1 3 4a1 1 0 0 1 1-1h3.5a1 1 0 0 1 1 1 11 11 0 0 0 .6 3.6 1 1 0 0 1-.25 1z"/></svg>
    <span>Phone: (530) 555-0182</span><span>|</span>
    <svg width="12" height="10" viewBox="0 0 24 18"><path fill="#fff" d="M0 0h24v18H0zM2 2v1l10 7 10-7V2z"/></svg>
    <span>Email : marla@brindlecovelaw.com</span>
  </div>
  <div class="abs social"><span></span><span></span><span></span></div>
</div>

<header class="abs header">
  <div class="abs brand">BRINDLE COVE P.C</div>
  <nav class="abs nav">
    <a class="active">HOME</a><a>ABOUT US</a><a>PRACTICE AREAS</a><a>ATTORNEYS</a><a>BLOG</a><a>CONTACT</a>
  </nav>
</header>

<section class="abs hero" role="img" aria-label="Photo of a suited attorney with crossed arms in a bright conference room">
  <h1 class="abs">BUSINESS<br>LAW</h1>
  <p class="abs">Find the big firm style legal counsel you can work with in your hometown</p>
  <div class="abs btn">Make an Appointment</div>
  <div class="abs dots"><span class="on"></span><span></span><span></span></div>
</section>

<section class="welcome">
  <div class="abs welcome-art" role="img" aria-label="Word cloud illustration around the words criminal law, justice and legal"></div>
  <h2 class="abs h2">Welcome to Brindle Cove P.C</h2>
  <div class="abs copy">
    <p>Find the big firm style legal counsel you can work with in your hometown region at Brindle Cove P.C., in Chico, CA. Attorney Marla J. Brindle, Esq., offers a boutique law firm opportunity for clients who want to enjoy all the advantages of her broad legal experience and education.</p>
    <p>She works closely with clients, and has the knowledge of many areas of law to apply to your situation. This is very helpful when it is necessary to incorporate those different areas of law practice into creating a winning argument for your unique case. Brindle Cove P.C. is owned by Marla J. Brindle, a dedicated and caring professional who uses her broad range of skills as a California lawyer to bring consumers and business</p>
  </div>
  <div class="abs btn">READ MORE</div>
</section>

<section class="abs practice">
  <h2 class="abs h2">Practice Areas</h2>

  <div class="abs area" style="left:130px;top:160px">
    <svg width="36" height="30" viewBox="0 0 36 30"><rect x="12" y="2" width="12" height="6" fill="none" stroke="#ec1f27" stroke-width="3"/><rect x="1" y="8" width="34" height="20" rx="2" fill="#ec1f27"/></svg>
    <h3>BUSINESS LAW</h3>
    <p>Small and medium-sized businesses have many of the same legal issues that affect large businesses</p>
  </div>
  <div class="abs area" style="left:463px;top:160px">
    <svg width="34" height="30" viewBox="0 0 34 30"><path d="M17 1 1 15h5v14h8v-9h6v9h8V15h5z" fill="#ec1f27"/></svg>
    <h3>REAL ESTATE LAW</h3>
    <p>Small and medium-sized businesses have many of the same legal issues that affect large businesses</p>
  </div>
  <div class="abs area" style="left:796px;top:160px">
    <svg width="28" height="34" viewBox="0 0 28 34"><path d="M1 1h18l8 8v24H1z" fill="#ec1f27"/><path d="M6 16h16M6 21h16M6 26h16" stroke="#fff" stroke-width="2"/></svg>
    <h3>BANKRUPTCY</h3>
    <p>Small and medium-sized businesses have many of the same legal issues that affect large businesses</p>
  </div>
  <div class="abs area" style="left:130px;top:298px">
    <svg width="38" height="32" viewBox="0 0 38 32"><circle cx="9" cy="8" r="5" fill="#ec1f27"/><circle cx="29" cy="8" r="5" fill="#ec1f27"/><circle cx="19" cy="12" r="6" fill="#ec1f27"/><path d="M1 26a8 8 0 0 1 16 0zM21 26a8 8 0 0 1 16 0zM9 31a10 10 0 0 1 20 0z" fill="#ec1f27"/></svg>
    <h3>FAMILY LAW</h3>
    <p>Small and medium-sized businesses have many of the same legal issues that affect large businesses</p>
  </div>
  <div class="abs area" style="left:463px;top:298px">
    <svg width="32" height="34" viewBox="0 0 32 34"><circle cx="16" cy="9" r="7" fill="#ec1f27"/><path d="M3 33a13 13 0 0 1 26 0z" fill="#ec1f27"/><rect x="12" y="22" width="8" height="6" fill="#fff"/></svg>
    <h3>CRIMINAL LAW</h3>
    <p>Small and medium-sized businesses have many of the same legal issues that affect large businesses</p>
  </div>
  <div class="abs area" style="left:796px;top:298px">
    <svg width="36" height="32" viewBox="0 0 36 32"><path d="M18 1 1 9h34z" fill="#ec1f27"/><rect x="3" y="11" width="30" height="3" fill="#ec1f27"/><rect x="6" y="15" width="4" height="11" fill="#ec1f27"/><rect x="13" y="15" width="4" height="11" fill="#ec1f27"/><rect x="20" y="15" width="4" height="11" fill="#ec1f27"/><rect x="27" y="15" width="4" height="11" fill="#ec1f27"/><rect x="1" y="27" width="34" height="4" fill="#ec1f27"/></svg>
    <h3>CIVIL LITIGATION</h3>
    <p>Small and medium-sized businesses have many of the same legal issues that affect large businesses</p>
  </div>
</section>

<section class="abs quote" role="img" aria-label="Dark photo of a hand signing a document at a desk">
  <blockquote class="abs">Brindle Cove is our go-to source for professional and sound legal advice. Brindle Cove has become a vital component to the success of our business as well as the businesses of the clients we have referred to Brindle Cove.</blockquote>
  <cite class="abs">– Ridgeway Accounting Partners –</cite>
  <div class="abs dots"><span></span><span class="on"></span><span></span></div>
</section>

<section class="blog">
  <h2 class="abs h2">Recent Blog</h2>
  <article class="abs post" style="left:130px;top:1790px">
    <div class="thumb" role="img" aria-label="Photo of business people meeting around a table"></div>
    <h3>OUR EXPECTATIONS</h3>
    <time>JUNE 25, 2016</time>
    <p>Attorney Marla Brindle is ready to help you reach positive outcomes during mediation and arbitration meetings, around the real estate settlement</p>
    <a>Read More »</a>
  </article>
  <article class="abs post" style="left:455px;top:1790px">
    <div class="thumb" role="img" aria-label="Photo of hands reviewing papers at a desk"></div>
    <h3>OUR REAL ESTATE</h3>
    <time>JUNE 25, 2016</time>
    <p>Attorney Marla Brindle is ready to help you reach positive outcomes during mediation and arbitration meetings, around the real estate settlement</p>
    <a>Read More »</a>
  </article>
  <article class="abs post" style="left:777px;top:1790px">
    <div class="thumb" role="img" aria-label="Photo of a team working together in an office"></div>
    <h3>OUR COMPANY EFFECTIVELY</h3>
    <time>JUNE 25, 2016</time>
    <p>Attorney Marla Brindle is ready to help you reach positive outcomes during mediation and arbitration meetings, around the real estate settlement</p>
    <a>Read More »</a>
  </article>
</section>

<section class="abs partners">
  <div class="abs badge" style="left:249px;width:210px"><span style="width:66px;height:66px;border-radius:50%;background:#4a6a9c"></span></div>
  <div class="abs badge" style="left:482px;width:209px"><span style="width:74px;height:74px;border-radius:50%;background:#8a8a8a"></span></div>
  <div class="abs badge" style="left:714px;width:235px"><span style="width:160px;height:34px;background:#2c4a7a"></span></div>
</section>

<section class="abs map" role="img" aria-label="Street map of the surrounding area"></section>
<section class="abs card">
  <h2 class="h2">Contact Us</h2>
  <p class="intro">Located in Chico, California, we serve clients throughout Northern California including Butte County, Tehama County, Plumas County, Glenn County, Colusa County, Sutter County, Yuba County</p>
  <div class="label" style="left:25px;top:164px">phone</div>
  <div class="value" style="left:25px;top:189px">
    <svg width="10" height="10" viewBox="0 0 24 24"><path fill="#333" d="M6.6 10.8a15 15 0 0 0 6.6 6.6l2.2-2.2a1 1 0 0 1 1-.25 11 11 0 0 0 3.6.6 1 1 0 0 1 1 1V20a1 1 0 0 1-1 1A17 17 0 0 1 3 4a1 1 0 0 1 1-1h3.5a1 1 0 0 1 1 1 11 11 0 0 0 .6 3.6 1 1 0 0 1-.25 1z"/></svg>(530) 555-0182</div>
  <div class="label" style="left:180px;top:164px">Email</div>
  <div class="value" style="left:180px;top:189px">
    <svg width="11" height="9" viewBox="0 0 24 18"><path fill="#333" d="M0 0h24v18H0zM2 2v1l10 7 10-7V2z"/></svg>marla@brindlecovelaw.com</div>
  <div class="label" style="left:25px;top:227px">Address</div>
  <div class="value" style="left:25px;top:252px">
    <svg width="9" height="12" viewBox="0 0 18 24"><path fill="#333" d="M9 0a9 9 0 0 0-9 9c0 7 9 15 9 15s9-8 9-15a9 9 0 0 0-9-9zm0 12a3 3 0 1 1 0-6 3 3 0 0 1 0 6z"/></svg>418 W 5th Street, Suite 300, Chico, CA 95928</div>

  <div class="field" style="top:50px">Your Name</div>
  <div class="field" style="top:106px">Your Email</div>
  <div class="field" style="top:171px">YourMessage</div>
  <div class="btn">SEND YOUR MESSAGE</div>
</section>

<footer class="abs footer">
  <div class="abs copy">2016 © brindle cove p.c. All Right Reserved.</div>
  <div class="abs social"><span></span><span></span><span></span></div>
</footer>

</body>
</html>
```